Create Flyer for RGB wall washers

We are launching a product that is run by an app and allows you to customize your exterior lighting at the touch of a button. We want to create the image of being technologically advanced company who is easy to work with. Looking for streamlined design which will reflect how we operate as a company. We will be printing at pressmarlow.com so please have the correct format. I am looking for this to be single sided thank you for your time and submission

Target Market(s)

Residential and commercial

Industry/Entity Type

Product

Requirements
Must have
• clean layout
• easy to read
• Common fonts
• Color scheme must work with logo (we can provide a black background to logo in needed)
Nice to have
• Nicely displayed images to help sell the idea
Should not have
• Too busy background

```html
<!DOCTYPE html>
<html lang="en">
<head>
<meta charset="utf-8">
<title>Brightfield Lighting – RGB Wall Washer Flyer</title>
<link rel="stylesheet" href="https://fonts.googleapis.com/css2?family=Anton&family=Questrial&family=Archivo+Black&family=Oswald:wght@400&family=Open+Sans:wght@600;800&display=swap">
<style>
  :root {
    --page-bg: #e6e7ea;
    --paper: #ffffff;
    --brand-blue: #2a63b8;
    --brand-blue-dark: #1d4f9c;
    --navy: #1b2d5c;
    --sky-light: #d8eef6;
    --sky-mid: #bfe2f1;
    --mist: #eef0f3;
    --ink: #141414;
    --steel: #7a8797;
  }
  * { box-sizing: border-box; margin: 0; padding: 0; }
  html, body { width: 1200px; height: 1017px; overflow: hidden; }
  body { background: var(--page-bg); position: relative; }

  .flyer {
    position: absolute; left: 229px; top: 28px;
    width: 742px; height: 960px;
    background: var(--paper);
    overflow: hidden;
    box-shadow: 0 6px 24px rgba(0,0,0,.18);
  }

  .masthead {
    position: absolute; left: 0; top: 0; width: 100%; height: 110px;
    display: flex; align-items: center; justify-content: center; gap: 14px;
  }
  .masthead .brand-mark {
    width: 34px; height: 34px; background: var(--brand-blue);
  }
  .masthead .brand-name {
    font-family: "Questrial", sans-serif; font-size: 34px;
    letter-spacing: 3px; color: var(--brand-blue); text-transform: uppercase;
  }

  .headline-band {
    position: absolute; left: 0; top: 110px; width: 100%; height: 112px;
    background: var(--brand-blue);
    text-align: center; color: #fff;
    font-family: "Anton", sans-serif; text-transform: uppercase;
    padding-top: 14px;
  }
  .headline-band .headline { font-size: 46px; line-height: 50px; letter-spacing: .5px; }
  .headline-band .subhead { font-size: 31px; line-height: 36px; }

  .body-panel {
    position: absolute; left: 0; top: 222px; width: 100%; height: 640px;
    background: linear-gradient(160deg, var(--sky-light) 0%, var(--sky-mid) 35%, var(--mist) 70%, #f3f3f4 100%);
  }

  .intro {
    position: absolute; left: 44px; top: 38px; width: 330px;
    font-family: "Questrial", sans-serif; font-size: 25px; line-height: 35px;
    color: var(--ink);
  }

  .photo {
    position: absolute; border-radius: 50%;
    border: 5px solid #fff;
    box-shadow: 0 3px 10px rgba(0,0,0,.2);
  }
  .photo-top { left: 400px; top: 20px; width: 300px; height: 300px;
    background: linear-gradient(180deg, #2d3c6e 0%, #8a5f9e 45%, #c39ab6 62%, #5a4a3a 100%); }
  .photo-left { left: 300px; top: 250px; width: 255px; height: 255px;
    background: linear-gradient(180deg, #3a2f55 0%, #a3476f 45%, #d46a7e 60%, #6a4a2c 100%); }
  .photo-right { left: 520px; top: 265px; width: 225px; height: 225px;
    background: linear-gradient(180deg, #3b4a5a 0%, #4fa07a 45%, #8a9a70 62%, #5a4a30 100%); }

  .price-badge {
    position: absolute; left: 487px; top: 405px; width: 160px; height: 160px;
    border-radius: 50%; background: var(--navy); border: 4px solid #fff;
    display: flex; flex-direction: column; align-items: center; justify-content: center;
    color: #fff; font-family: "Open Sans", sans-serif;
  }
  .price-badge .price-label { font-size: 17px; font-weight: 600; }
  .price-badge .price-value { font-size: 46px; font-weight: 800; line-height: 50px; }

  .app-screens {
    position: absolute; left: 40px; top: 340px; width: 250px; height: 190px;
    border-radius: 10px;
    background: linear-gradient(90deg, #f2f2f4 0%, #c9c9d0 40%, #8b86a8 70%, #e7e7ea 100%);
  }

  .call-line {
    position: absolute; left: 44px; top: 560px;
    display: flex; align-items: baseline; gap: 18px;
  }
  .call-line .call-label { font-family: "Oswald", sans-serif; font-size: 46px; color: var(--ink); }
  .call-line .phone { font-family: "Archivo Black", sans-serif; font-size: 60px;
    color: var(--brand-blue); letter-spacing: 3px; }

  .footer-band {
    position: absolute; left: 0; bottom: 0; width: 100%; height: 98px;
    background: var(--brand-blue);
    display: flex; align-items: center; justify-content: flex-end; padding-right: 50px;
  }
  .footer-band .website { font-family: "Open Sans", sans-serif; font-weight: 600;
    font-size: 22px; color: #fff; }
</style>
</head>
<body>
  <article class="flyer">
    <header class="masthead">
      <span class="brand-mark"></span>
      <span class="brand-name">Brightfield Lighting</span>
    </header>

    <section class="headline-band">
      <h1 class="headline">Control your outdoor lighting</h1>
      <p class="subhead">with the touch of a button</p>
    </section>

    <section class="body-panel">
      <p class="intro">State-of-the-Art lighting system that will wash your exterior walls with light or landscape plantings with up-lights. Its year-round lighting at a fraction of the cost.</p>

      <div class="photo photo-top" role="img" aria-label="House facade at night washed in purple and pink light"></div>
      <div class="photo photo-left" role="img" aria-label="House facade at night lit in magenta and red tones"></div>
      <div class="photo photo-right" role="img" aria-label="House facade at night lit in green and red tones"></div>

      <div class="price-badge">
        <span class="price-label">starting at</span>
        <span class="price-value">$799</span>
      </div>

      <div class="app-screens" role="img" aria-label="Row of smartphones showing the colour-control app screens"></div>

      <div class="call-line">
        <span class="call-label">Call:</span>
        <span class="phone">404 555 0137</span>
      </div>
    </section>

    <footer class="footer-band">
      <span class="website">www.brightfield-lighting.com</span>
    </footer>
  </article>
</body>
</html>
```